Cole Varga Photography

Would like the Business card to have a cool logo. I’m targeting wedding/ engagement: portrait photography. My phone number on it. And my business email address.

Wedding/portrait/engagement photography.

```html
<!DOCTYPE html>
<html lang="en">
<head>
<meta charset="utf-8">
<title>Cole Varga Photography – Business Card</title>
<link rel="stylesheet" href="https://fonts.googleapis.com/css2?family=Poppins:wght@400;500;600&display=swap">
<style>
  :root {
    --backdrop: #2a2a2c;
    --card: #0b0b0c;
    --card-edge: #1c1c1e;
    --pink: #e6218a;
    --teal: #2fa3c9;
    --white: #f2f2f2;
    --rule: #bdbdbd;
  }
  * { box-sizing: border-box; margin: 0; padding: 0; }
  html, body {
    width: 1200px;
    height: 900px;
    overflow: hidden;
    background: var(--backdrop);
    font-family: "Poppins", sans-serif;
  }
  .sheet {
    width: 1200px;
    height: 900px;
    display: flex;
    flex-direction: column;
    align-items: center;
    justify-content: center;
    gap: 40px;
  }
  .card {
    width: 700px;
    height: 400px;
    background: radial-gradient(ellipse at 35% 35%, #18181a 0%, var(--card) 70%);
    border: 1px solid var(--card-edge);
    position: relative;
    box-shadow: 0 18px 40px rgba(0,0,0,.55);
  }

  /* Front */
  .card-front {
    display: flex;
    flex-direction: column;
    align-items: center;
    justify-content: center;
  }
  .brand {
    display: flex;
    align-items: center;
    gap: 16px;
  }
  .brand-dot {
    width: 34px;
    height: 34px;
    border-radius: 50%;
    background: var(--teal);
    flex: none;
  }
  .brand-name {
    font-weight: 500;
    font-size: 36px;
    color: var(--pink);
    letter-spacing: .5px;
  }
  .services {
    margin-top: 34px;
    font-weight: 600;
    font-size: 15px;
    letter-spacing: 1.4px;
    text-transform: uppercase;
    color: var(--pink);
  }
  .services .sep { margin: 0 8px; }

  /* Back */
  .card-back {
    display: flex;
    align-items: center;
    padding: 0 60px 0 70px;
  }
  .card-back .brand {
    flex-direction: column;
    gap: 12px;
    width: 230px;
  }
  .card-back .brand-dot { width: 70px; height: 70px; }
  .card-back .brand-name {
    font-size: 22px;
    text-align: center;
    line-height: 1.3;
  }
  .divider {
    width: 1px;
    height: 170px;
    background: var(--rule);
    margin: 0 40px 0 30px;
  }
  .contact { list-style: none; display: flex; flex-direction: column; gap: 14px; }
  .contact-item {
    display: flex;
    align-items: center;
    gap: 12px;
    color: var(--white);
    font-size: 17px;
    font-weight: 400;
  }
  .contact-icon { width: 16px; height: 16px; flex: none; }
</style>
</head>
<body>
<main class="sheet">

  <section class="card card-front" aria-label="Business card front">
    <div class="brand">
      <span class="brand-dot"></span>
      <span class="brand-name">Cole Varga Photography</span>
    </div>
    <p class="services">Wedding<span class="sep">•</span>Portrait<span class="sep">•</span>Engagement Photography</p>
  </section>

  <section class="card card-back" aria-label="Business card back">
    <div class="brand">
      <span class="brand-dot"></span>
      <span class="brand-name">Cole Varga Photography</span>
    </div>
    <span class="divider"></span>
    <ul class="contact">
      <li class="contact-item">
        <svg class="contact-icon" viewBox="0 0 24 24" aria-hidden="true">
          <path fill="#e6218a" d="M6.6 10.8a15.1 15.1 0 0 0 6.6 6.6l2.2-2.2a1 1 0 0 1 1-.25 11.4 11.4 0 0 0 3.6.57 1 1 0 0 1 1 1V20a1 1 0 0 1-1 1A17 17 0 0 1 3 4a1 1 0 0 1 1-1h3.5a1 1 0 0 1 1 1c0 1.25.2 2.45.57 3.6a1 1 0 0 1-.25 1z"/>
        </svg>
        <span>0123-4567-8910</span>
      </li>
      <li class="contact-item">
        <svg class="contact-icon" viewBox="0 0 24 24" aria-hidden="true">
          <rect x="2" y="5" width="20" height="14" rx="1.5" fill="#e6218a"/>
          <path d="M3 6.5l9 6.5 9-6.5" fill="none" stroke="#0b0b0c" stroke-width="1.8"/>
        </svg>
        <span>info@ColeVargaPhotography.com</span>
      </li>
    </ul>
  </section>

</main>
</body>
</html>
```